Design for three pages of a 12-page 4-color 8.5 x 11 magazine-type booklet

We will be taking the information from a webpage at glowmerestudies.org and putting it into a 12-page 4-color 8.5 x 11 magazine-type booklet that will look like an upscale company report. I need to have a design in Photoshop for the cover and two inside pages that I can use as the template for the pages. I likely will also need help putting it together once I start putting the contents into the pages. I may just decide on the content and have the designer create the booklet as an additional freelance contract. First, I need a design for (1) the front cover, (2) one information page taken from information on http://www.glowmerestudies.org/kvon-project-management-staff/, and (3) one of the pages that has a researcher from this page on it: http://www.glowmerestudies.org/teaching-people-how-to-have/. That's designs for three pages. The designs have to be very professional looking and businesslike. We will be using the booklet to pitch to foundations and philanthropists. The work on the publication itself would be additional freelance work on an hourly basis.

Serif

• Professional look

```html
<!DOCTYPE html>
<html lang="en">
<head>
<meta charset="utf-8">
<title>KVON Booklet – Cover and Inside Pages</title>
<link rel="stylesheet" href="https://fonts.googleapis.com/css2?family=Orbitron:wght@800&family=Montserrat:wght@500;700;800&family=Open+Sans:wght@400;600;700&display=swap">
<style>
:root{
  --blue:#1b1ba8;
  --ink:#262626;
  --grey-dark:#55565a;
  --grey-mid:#8b8c90;
  --grey-light:#d9d9db;
  --paper:#fbfbfb;
  --backdrop:#e8e2dc;
  --photo-a:#c9c3bb;
  --photo-b:#6d6660;
}
*{margin:0;padding:0;box-sizing:border-box}
html,body{width:880px;height:1200px;overflow:hidden}
body{background:var(--backdrop);font-family:"Open Sans",Arial,sans-serif;color:var(--ink);position:relative}
.row{position:absolute;left:0;width:880px;height:392px}
.row--covers{top:4px}
.row--staff{top:404px}
.row--report{top:804px}
.page{position:absolute;top:2px;width:300px;height:388px;background:var(--paper);overflow:hidden;box-shadow:0 2px 8px rgba(0,0,0,.18)}
.page--left{left:140px}
.page--right{left:440px}
.row--covers .page--left{left:118px}
.row--covers .page--right{left:462px}
.spine{position:absolute;left:439px;top:2px;width:2px;height:388px;background:linear-gradient(90deg,rgba(0,0,0,.18),rgba(0,0,0,0));z-index:2}
svg{display:block}
.logo-word{font-family:"Montserrat",sans-serif;font-weight:800;fill:var(--blue);letter-spacing:1px}
.cover-title{font-family:"Orbitron",sans-serif;font-weight:800;letter-spacing:.5px}
.cover-tagline{font-family:"Open Sans",sans-serif;font-weight:600;font-size:7.6px;fill:var(--blue)}
.contact{font-family:"Open Sans",sans-serif;font-size:7.6px;fill:var(--ink)}

/* inside pages */
.band{position:absolute;height:13px;background:var(--blue);color:#fff;font-family:"Montserrat",sans-serif;font-weight:700;font-size:7px;letter-spacing:.8px;line-height:13px;padding-left:14px;clip-path:polygon(6px 0,100% 0,calc(100% - 6px) 100%,0 100%)}
.people{position:absolute;display:grid;grid-template-columns:repeat(3,82px);column-gap:8px;row-gap:12px}
.person{display:flex;flex-direction:column;align-items:center}
.portrait{position:relative;width:80px;height:76px;background:linear-gradient(160deg,var(--photo-a),var(--photo-b));border:2px solid #fff;box-shadow:0 1px 2px rgba(0,0,0,.25)}
.portrait--books{background:linear-gradient(160deg,#5a6a8c,#8a6a3a)}
.caption{position:absolute;left:0;right:0;bottom:0;background:rgba(85,86,90,.88);color:#fff;text-align:center;font-size:4.4px;line-height:5.2px;padding:1px 0}
.caption b{display:block;font-family:"Montserrat",sans-serif;font-size:5.8px;line-height:6.6px}
.bio{margin-top:5px;width:100%;font-size:5.3px;line-height:6.8px;text-align:justify;color:#333}

.flow{position:absolute;left:18px;top:16px;width:264px;font-size:5.4px;line-height:6.9px;color:#333;text-align:justify}
.flow p+p{margin-top:3px}
.flow-section{margin-top:10px}
.intro{display:flex;gap:8px}
.intro-side{flex:0 0 48px;font-size:4.4px;line-height:5.4px;text-align:left}
.mini-portrait{width:48px;height:56px;background:linear-gradient(160deg,var(--photo-a),var(--photo-b));border:1.5px solid #fff;box-shadow:0 1px 2px rgba(0,0,0,.25);margin-bottom:2px}
.head-bar{display:inline-block;height:10px;background:var(--blue);color:#fff;font-family:"Montserrat",sans-serif;font-weight:700;font-size:5.8px;letter-spacing:.4px;line-height:10px;padding:0 12px 0 6px;margin-bottom:4px;clip-path:polygon(0 0,100% 0,calc(100% - 5px) 100%,0 100%)}
.small-head{font-family:"Montserrat",sans-serif;font-weight:700;font-size:5.6px;color:var(--ink);margin:6px 0 2px}
.bullets{list-style:none}
.bullets li{position:relative;padding-left:6px}
.bullets li::before{content:"";position:absolute;left:1px;top:2.6px;width:2px;height:2px;border-radius:50%;background:var(--blue)}
.timeline{font-family:"Montserrat",sans-serif;font-weight:700;font-size:6.6px;color:var(--ink);margin:10px 0 4px}
.timeline span{color:var(--blue)}
.visual{height:96px;background:radial-gradient(ellipse at 45% 60%,#f4e6c8 0%,#8a7a5e 28%,#3e3830 60%,#2a2622 100%)}
.costs-title{font-family:"Montserrat",sans-serif;font-weight:800;font-size:6.4px;color:var(--blue);margin:8px 0 2px}
.costs-wrap{display:flex;gap:40px}
.costs{border-collapse:collapse;font-family:"Montserrat",sans-serif;font-size:5.2px;font-weight:700;color:var(--ink)}
.costs td{padding:1.8px 0}
.costs td.num{text-align:right;padding-left:12px}
</style>
</head>
<body>

<section class="row row--covers">
  <article class="page page--left cover-front">
    <svg width="300" height="388" viewBox="0 0 300 388">
      <defs>
        <linearGradient id="coverPaper" x1="0" y1="0" x2="1" y2="1">
          <stop offset="0" stop-color="#ffffff"/><stop offset="1" stop-color="#e6e6e8"/>
        </linearGradient>
        <radialGradient id="tunnelLight" cx="0.7" cy="0.5" r="0.7">
          <stop offset="0" stop-color="#ffffff"/><stop offset=".55" stop-color="#d6d6d6"/><stop offset="1" stop-color="#5a5a5a"/>
        </radialGradient>
      </defs>
      <rect width="300" height="388" fill="url(#coverPaper)"/>
      <text class="logo-word" x="26" y="52" font-size="28">KVON</text>
      <polygon points="0,72 300,72 300,96 0,96" fill="var(--grey-light)"/>
      <polygon points="0,104 132,104 30,268 0,268" fill="var(--grey-dark)"/>
      <polygon points="220,104 300,104 300,140 240,140" fill="var(--grey-dark)"/>
      <g role="img" aria-label="Photo of a silhouetted man walking toward bright light at the end of a corridor">
        <polygon points="140,106 300,106 300,250 250,282 40,282" fill="url(#tunnelLight)" stroke="#111" stroke-width="5"/>
      </g>
      <polygon points="0,290 118,388 0,388" fill="var(--blue)"/>
      <g class="cover-text" transform="rotate(-9 210 330)">
        <text class="cover-title" x="100" y="303" font-size="13" fill="var(--ink)">BRIDGING <tspan fill="var(--blue)">HEAVEN</tspan></text>
        <text class="cover-title" x="128" y="323" font-size="18" fill="var(--ink)">AND EARTH</text>
        <text class="cover-tagline" x="288" y="337" text-anchor="end">When all people realize we are eternal</text>
        <text class="cover-tagline" x="288" y="346" text-anchor="end">Beings, humankind will live together in</text>
        <text class="cover-tagline" x="288" y="355" text-anchor="end">love, peace and joy</text>
        <rect x="122" y="362" width="220" height="15" fill="var(--grey-dark)"/>
        <text x="286" y="372.5" text-anchor="end" font-family="Open Sans, sans-serif" font-weight="600" font-size="7.6" fill="#fff">www.glowmerestudies.org</text>
      </g>
    </svg>
  </article>

  <article class="page page--right cover-back">
    <svg width="300" height="388" viewBox="0 0 300 388">
      <defs>
        <linearGradient id="backPaper" x1="0" y1="0" x2="0" y2="1">
          <stop offset="0" stop-color="#f2f2f4"/><stop offset="1" stop-color="#ffffff"/>
        </linearGradient>
        <linearGradient id="skyFill" x1="0" y1="0" x2="1" y2="1">
          <stop offset="0" stop-color="#8fb0d6"/><stop offset=".5" stop-color="#d9e6f2"/><stop offset="1" stop-color="#9ab6d8"/>
        </linearGradient>
      </defs>
      <rect width="300" height="388" fill="url(#backPaper)"/>
      <polygon points="236,0 300,0 300,230 262,230" fill="var(--grey-mid)"/>
      <polygon points="220,0 300,0 300,96" fill="var(--blue)"/>
      <g role="img" aria-label="Photo of a stairway rising through clouds into a blue sky">
        <polygon points="52,56 226,56 264,242 52,242" fill="url(#skyFill)" stroke="#111" stroke-width="5"/>
      </g>
      <text class="logo-word" x="30" y="306" font-size="24">KVON</text>
      <line x1="134" y1="274" x2="134" y2="340" stroke="var(--grey-mid)" stroke-width="0.8"/>
      <g fill="var(--ink)">
        <path d="M147 281c1 2 3 4 5 5l1.5-1.5c.3-.3.6-.3.9-.2l2 .8c.3.1.5.4.5.7v2c0 .4-.3.7-.7.7-5 0-9.5-4.5-9.5-9.5 0-.4.3-.7.7-.7h2c.3 0 .6.2.7.5l.8 2c.1.3 0 .6-.2.9z"/>
        <rect x="146" y="295" width="10" height="7" rx="1"/>
        <path d="M151 310a3.6 3.6 0 0 0-3.6 3.6c0 2.6 3.6 6.4 3.6 6.4s3.6-3.8 3.6-6.4A3.6 3.6 0 0 0 151 310zm0 5a1.4 1.4 0 1 1 0-2.8 1.4 1.4 0 0 1 0 2.8z"/>
      </g>
      <polyline points="146,295.5 151,299.5 156,295.5" fill="none" stroke="#fff" stroke-width=".8"/>
      <text class="contact" x="162" y="288">800 555-0147</text>
      <text class="contact" x="162" y="302">info@glowmerestudies.org</text>
      <text class="contact" x="162" y="317">48 Linden Court, Fairvale, IL 61799</text>
    </svg>
  </article>
</section>

<section class="row row--staff">
  <article class="page page--left staff-page">
    <div class="band" style="left:40px;top:14px;width:244px">KVON PROJECT MANAGEMENT STAFF</div>
    <div class="people" style="left:20px;top:38px">
      <div class="person">
        <div class="portrait" role="img" aria-label="Portrait of the project director"><div class="caption"><b>Project Director</b>R. Calder Hume, PhD</div></div>
        <p class="bio">Dr. Hume is the president of KVON. His PhD is in supervision and educational program development. He is the co-author of several books on consciousness and has been a manager of communications at a telephone company, an administrator of a graduate school and owner and manager of two companies.</p>
      </div>
      <div class="person">
        <div class="portrait" role="img" aria-label="Portrait of the finance lead"><div class="caption"><b>Finance</b>Lena Ashby</div></div>
        <p class="bio">Lena Ashby was employed for 21 years by the Department of Defense, where she was awarded a Professional Performance Award. She then helped develop an expanding retail chain operation and later served as a financial manager for a major regional distribution company.</p>
      </div>
      <div class="person">
        <div class="portrait" role="img" aria-label="Portrait of the administration lead"><div class="caption"><b>Administration</b>Katrin Moss</div></div>
        <p class="bio">Katrin Moss has been CEO of a regional psychological service and a national consulting firm. She provides operations leadership, is a board member of a community foundation and has served on the board of directors of a chamber of commerce.</p>
      </div>
      <div class="person">
        <div class="portrait" role="img" aria-label="Portrait of the media lead"><div class="caption"><b>Media</b>Sonia Chandler</div></div>
        <p class="bio">Sonia Chandler is the founder and producer of Beyond Today Radio. She is the author of a bestselling guide to life after loss, which encourages readers to ease their grief and make the most of every day. She brings her experience in producing a radio show to KVON.</p>
      </div>
      <div class="person">
        <div class="portrait" role="img" aria-label="Portrait of the education lead"><div class="caption"><b>Education</b>Ron Belgrave</div></div>
        <p class="bio">Ron Belgrave was employed for 21 years by a national training institute, where he designed adult learning programs. He then helped develop an online education platform and manages course design, tutorials and learner support.</p>
      </div>
      <div class="person">
        <div class="portrait portrait--books" role="img" aria-label="Photo of published book covers"><div class="caption"><b>Publications</b>Wider Horizon Publications</div></div>
        <p class="bio">Wider Horizon Publications is a wholly owned publishing company that releases books on grief, guided connections and the continuity of life, including workbooks, tutorials and a series of accounts from experiencers.</p>
      </div>
    </div>
  </article>

  <div class="spine"></div>

  <article class="page page--right board-page">
    <div class="band" style="left:16px;top:14px;width:250px">KVON RESEARCH ADVISORY BOARD</div>
    <div class="people" style="left:18px;top:38px">
      <div class="person">
        <div class="portrait" role="img" aria-label="Portrait of an advisory board member"><div class="caption"><b>Anne Corwell, PhD</b></div></div>
        <p class="bio">Dr. Anne Corwell is the Director of Research for a center studying life between lives. She co-authored a book of life between lives and holds a PhD from a major university. She directed a nursing research center and served as a research scientist in several university medical centers.</p>
      </div>
      <div class="person">
        <div class="portrait" role="img" aria-label="Portrait of an advisory board member"><div class="caption"><b>Dana Smythe-Mercer, MA</b></div></div>
        <p class="bio">Dana Smythe-Mercer is founder and owner of a research firm. She has over 20 years of experience conducting evaluation research for government ministries and agencies, and has provided research advice to non-profit organizations and private consulting firms.</p>
      </div>
      <div class="person">
        <div class="portrait" role="img" aria-label="Portrait of an advisory board member"><div class="caption"><b>Einar Holmsson, PhD</b></div></div>
        <p class="bio">Dr. Holmsson has a PhD in psychology. He is Emeritus Professor at a national university and a researcher with a psychical research society. He has published five books and many papers and has received awards for his contributions to the field.</p>
      </div>
    </div>
    <div class="people" style="left:40px;top:206px;grid-template-columns:repeat(2,104px);column-gap:20px">
      <div class="person">
        <div class="portrait" role="img" aria-label="Portrait of an advisory board member"><div class="caption"><b>Jon Vanderlee, PhD</b></div></div>
        <p class="bio">Dr. Jon Vanderlee completed his undergraduate work in physics and earned an MSc and PhD in physics, studying the thermal properties of diamonds. He was an Associate Professor and has published more than 80 scientific articles.</p>
      </div>
      <div class="person">
        <div class="portrait" role="img" aria-label="Portrait of an advisory board member"><div class="caption"><b>Werner Sallow, MD, MPH</b></div></div>
        <p class="bio">Dr. Sallow is a Board Certified Occupational Medicine physician who was assistant chief of occupational medicine at a regional medical center. He served as medical director for a large company and earned a master of public health.</p>
      </div>
    </div>
  </article>
</section>

<section class="row row--report">
  <article class="page page--left report-page">
    <div class="flow">
      <div class="intro">
        <div class="intro-side">
          <div class="mini-portrait" role="img" aria-label="Portrait of the project director"></div>
          <b>Project Director</b><br>R. Calder Hume, PhD
        </div>
        <div>
          <p>Calder Hume, president of KVON, has developed an online training program that enables anyone to connect with loved ones living on the next plane of life. It uses a form of self-relaxation to bring the experiencer into a state in which the connections may occur. It then teaches the experiencer how to allow free, open unfoldment so messages can come through from the loved one. The experiencer fills out journals after each stage, which are submitted to KVON. Calder reads each journal and coaches experiencers to help them learn how to have an afterlife connection by allowing free unfoldment.</p>
          <p>The procedure is free on the Internet at this link: Guided Connection Method.</p>
        </div>
      </div>

      <div class="flow-section">
        <div class="head-bar">SUCCESSES AND VALIDATIONS</div>
        <p>Approximately 86% of those who go through the stages in the training have afterlife connections. The method is named the Guided Connection Method. It is available through any standard Web browser on the Internet and is free. The method has now been experienced by thousands of people. We continue to evaluate and refine it to help people learn how to make their own afterlife connections with loved ones.</p>
        <p>You can read the report about the procedure and study, containing accounts of actual guided connections at this link: Read the study.</p>
        <p>To read additional accounts of guided connections, go to this link: Additional accounts of connections.</p>
        <p>To read accounts that resulted in validations, such as when the experiencer learned things he or she could not have known that were discovered to be true, go to this link: Validations.</p>
      </div>

      <div class="flow-section">
        <div class="head-bar">EXAMPLE ACCOUNT BY AN EXPERIENCER</div>
        <p>I went to the same garden (my own) and again found what I did not expect. My uncle, who died about the same time as my father, was sitting in the seat by my brother. He had been my favorite uncle when I grew up. He used to take me for rides in his truck when he was working. I have not thought of him for some time. He began talking to me about the farm where I grew up. We walked out from the farmhouse and he began sharing about how it was when he grew up there.</p>
        <p>I had not thought of that much; both he and my dad spent their childhood there. I turned to look at the ridge where I used to walk and daydream. Immediately he took both of us to the ridge. He said it was one of his favorite places too. Then he talked about how they dug out the white chalk rock there to make my grandmother's flower beds.</p>
        <p>It was a revelation to me: I had always loved the raised round flower beds in the front yard and always loved the broken up place on the ridge but I had never put two and two together. Then he took me up high to look down on the farm. He asked me if I would like to take care of a farm for my remaining years. I said it was a bit odd to do that. He waited for me to answer. I said "Sure." It seemed and still seems a strange idea. We left it there, said goodbye and separated.</p>
      </div>
    </div>
  </article>

  <div class="spine"></div>

  <article class="page page--right report-page">
    <div class="flow">
      <p>Not what I expected. Just a chatty visit with someone I had not seen for some time. I still don't know what to think of his question. Different members of my family have been showing up. We were never an overly affectionate bunch. All three sessions have seemed to convey a rather amused and affectionate attitude towards me. I have felt very much at home with them, always felt surprised at what transpires and left wondering at them in a good way.</p>

      <div class="flow-section">
        <div class="head-bar">FUTURE ADVANCEMENTS WITH FUNDING</div>
        <p>With funding, the model can be expanded to allow more people to learn how to have successful afterlife communication. The procedure can be refined to be even more successful. As a result, this medium will have a profound effect on many people's level of grief, their understanding of who they are in eternity, and their relationships with other people in their lives.</p>
        <div class="small-head">Funding will make possible</div>
        <ul class="bullets">
          <li>Validating the procedure to demonstrate that the connections are valid connections with loved ones</li>
          <li>Studying the procedure to determine how it can be refined to improve afterlife communication</li>
          <li>Translating the procedures into French and Spanish</li>
        </ul>
      </div>

      <div class="timeline">TIMELINE: <span>12 MONTHS</span></div>
      <div class="visual" role="img" aria-label="Image of cupped hands holding a glowing light surrounded by a word cloud with LOVE at the centre"></div>

      <div class="costs-title">COSTS</div>
      <div class="costs-wrap">
        <table class="costs">
          <tr><td>MEDIUMS FOR VALIDATION</td><td class="num">5</td></tr>
          <tr><td>SESSIONS PER MEDIUM</td><td class="num">5</td></tr>
          <tr><td>TOTAL SESSIONS</td><td class="num">25</td></tr>
          <tr><td>COST/SESSION</td><td class="num">$300</td></tr>
          <tr><td>TOTAL MEDIUM COSTS</td><td class="num">$7500</td></tr>
        </table>
        <table class="costs">
          <tr><td>STATISTICIAN</td><td class="num">$2000</td></tr>
          <tr><td>PROJECT MANAGEMENT</td><td class="num">$3000</td></tr>
          <tr><td>RECORDING AND ANALYSIS</td><td class="num">$3000</td></tr>
          <tr><td>PROJECT TOTAL</td><td class="num">$15500</td></tr>
        </table>
      </div>
    </div>
  </article>
</section>

</body>
</html>
```